Professional Business Cards

We need a nice looking, profession and modern business card for our new company. Our logo is attatched

Target Market(s)

Young Professionals

Industry/Entity Type

Financial

Contact Information for Business Card

FRONT

Vardane Ledger Pty Ltd
Level 22, Harbour Point, 48 Wattlebrook Ave
Sydney NSW 2000
ABN : 47 318 905 226

Owen Hadley - Chief Operations Officer
P : 02 9173 5528
M: 0418 356 091
owen@vardaneledger,com

BACK

- Cryptocurrency Exchange Services
- Cryptocurrency Mining Operations
- Cryptocurrency Investment Fund Offering

Font styles to use
Sans Serif

Colors
0255a3
9d9d9d

```html
<!DOCTYPE html>
<html lang="en">
<head>
<meta charset="utf-8">
<title>Vardane Ledger – Business Card</title>
<link href="https://fonts.googleapis.com/css2?family=Montserrat:wght@400;500;600;700&display=swap" rel="stylesheet">
<style>
  :root {
    --brand-blue: #0255a3;
    --brand-grey: #9d9d9d;
    --ink: #4a4a4a;
    --paper: #ffffff;
    --backdrop: #2b2b2b;
  }
  * { margin: 0; padding: 0; box-sizing: border-box; }
  html, body { width: 1200px; height: 864px; overflow: hidden; }
  body {
    background: var(--backdrop);
    font-family: "Montserrat", Arial, sans-serif;
    position: relative;
  }
  .card {
    position: absolute;
    top: 267px;
    width: 540px;
    height: 330px;
    border-radius: 18px;
    overflow: hidden;
  }
  /* Back side */
  .card-back { left: 40px; background: var(--brand-blue); color: var(--paper); }
  .card-back .wordmark {
    position: absolute; left: 44px; top: 52px;
    display: flex; align-items: center; gap: 12px;
  }
  .wordmark { display: flex; align-items: center; white-space: nowrap; }
  .wordmark .mark-square { width: 26px; height: 26px; background: currentColor; flex: none; }
  .wordmark .name {
    font-weight: 700; font-size: 30px; letter-spacing: 1px; text-transform: uppercase;
  }
  .card-back .abn {
    position: absolute; right: 40px; top: 200px;
    font-size: 13px; font-weight: 500; letter-spacing: .3px;
  }
  .services {
    position: absolute; left: 44px; bottom: 40px;
    list-style: none; font-size: 15px; line-height: 1.55;
  }
  .services li { display: flex; align-items: center; gap: 10px; }
  .services li::before {
    content: ""; width: 9px; height: 9px; background: var(--paper);
  }
  /* Front side */
  .card-front { left: 620px; background: var(--paper); }
  .card-front .wordmark {
    position: absolute; left: 28px; top: 180px; gap: 8px; color: var(--brand-blue);
  }
  .card-front .wordmark .mark-square { width: 20px; height: 20px; }
  .card-front .wordmark .name { font-size: 19px; letter-spacing: .5px; }
  .divider {
    position: absolute; left: 280px; top: 80px;
    width: 2px; height: 210px; background: var(--brand-blue);
  }
  .details { position: absolute; left: 298px; top: 76px; color: var(--ink); }
  .person-name { font-size: 22px; font-weight: 700; color: var(--brand-blue); }
  .person-title { font-size: 13px; color: #6a6a6a; margin-top: 1px; }
  .address { font-size: 13px; line-height: 1.45; margin-top: 18px; font-style: normal; }
  .contacts { list-style: none; margin-top: 14px; font-size: 13px; line-height: 1.65; }
  .contacts li { display: flex; align-items: center; gap: 8px; white-space: nowrap; }
  .contacts svg { width: 13px; height: 13px; flex: none; fill: var(--brand-blue); }
</style>
</head>
<body>
  <section class="card card-back" aria-label="Card back">
    <div class="wordmark"><span class="mark-square"></span><span class="name">Vardane Ledger</span></div>
    <p class="abn">ABN : 47 318 905 226</p>
    <ul class="services">
      <li>Cryptocurrency Exchange Services</li>
      <li>Cryptocurrency Mining Operations</li>
      <li>Cryptocurrency Investment Fund Offering</li>
    </ul>
  </section>

  <section class="card card-front" aria-label="Card front">
    <div class="wordmark"><span class="mark-square"></span><span class="name">Vardane Ledger</span></div>
    <div class="divider"></div>
    <div class="details">
      <p class="person-name">Owen Hadley</p>
      <p class="person-title">Chief Operations Officer</p>
      <address class="address">Level 22, Harbour Point<br>48 Wattlebrook Ave<br>Sydney NSW 2000</address>
      <ul class="contacts">
        <li><svg viewBox="0 0 16 16"><path d="M3 1h3l1.5 4-2 1.3a9 9 0 0 0 4.2 4.2L11 8.5l4 1.5v3a2 2 0 0 1-2 2A12 12 0 0 1 1 3a2 2 0 0 1 2-2z"/></svg>02 9173 5528</li>
        <li><svg viewBox="0 0 16 16"><path d="M4 0h8a1 1 0 0 1 1 1v14a1 1 0 0 1-1 1H4a1 1 0 0 1-1-1V1a1 1 0 0 1 1-1zm1 2v10h6V2zm3 11a1 1 0 1 0 0 2 1 1 0 0 0 0-2z"/></svg>0418 356 091</li>
        <li><svg viewBox="0 0 16 16"><path d="M0 3h16v10H0zm1.5 1.2v.3L8 9l6.5-4.5v-.3z"/></svg>owen@vardaneledger,com</li>
        <li><svg viewBox="0 0 16 16"><path d="M8 0a8 8 0 1 0 0 16A8 8 0 0 0 8 0zm0 1.5c1 0 2 1.9 2.3 4.5H5.7C6 3.4 7 1.5 8 1.5zM1.6 7h3a14 14 0 0 0 0 2h-3a6.5 6.5 0 0 1 0-2zm4.1 0h4.6a12 12 0 0 1 0 2H5.7a12 12 0 0 1 0-2zm5.7 0h3a6.5 6.5 0 0 1 0 2h-3a14 14 0 0 0 0-2zM5.7 10h4.6C10 12.6 9 14.5 8 14.5S6 12.6 5.7 10z"/></svg>www.vardaneledger.com</li>
      </ul>
    </div>
  </section>
</body>
</html>
```